Interfaith organization needs a poster advertising event for youth

We need a poster advertising our annual Lantern Gathering and Summit, where youth of all different religions come together for dialogue, friendship, fun, art, and musical performances. The poster should be have a front advertising the event, and the back should have more detailed descriptions of the event and submissions. It should be fun and eye catching!

Target Market(s)

Youth and Religious Organizations

Industry/Entity Type

Festival

Font styles to use
Serif

Requirements
Must have
• Pictures, poster-feel, contact information, etc. Logos of Bright Harbor Allies and Shared Paths Youth Circle of Willow Basin

```html
<!DOCTYPE html>
<html lang="en">
<head>
<meta charset="utf-8">
<title>Lantern Gathering and Summit – Poster</title>
<link href="https://fonts.googleapis.com/css2?family=Cinzel:wght@400;500&family=Merriweather:wght@400;700;900&display=swap" rel="stylesheet">
<style>
:root{
  --stage:#262626;
  --paper:#ffffff;
  --ink:#1a1a1a;
  --forest:#1f4d3a;
  --gold:#e9b649;
  --seal:#a8823a;
  --orange:#f4a63e;
  --night:#050505;
  --harbor:#3f8fd0;
  --mist-top:#ffffff;
  --mist-bottom:#dcdcdc;
}
*{margin:0;padding:0;box-sizing:border-box}
html,body{width:1200px;height:923px;overflow:hidden;background:var(--stage)}
.page{position:absolute;top:92px;width:514px;height:738px;overflow:hidden}
.front{left:77px;background:var(--paper)}
.back{left:612px;background:linear-gradient(180deg,var(--mist-top) 20%,var(--mist-bottom) 75%)}

/* front */
.council-name{position:absolute;top:26px;left:0;width:100%;text-align:center;font-family:'Cinzel',serif;font-size:15px;letter-spacing:.5px;color:var(--ink)}
.seal{position:absolute;left:38px;top:64px;width:118px;height:118px;border:2px solid var(--seal);border-radius:50%;display:flex;align-items:center;justify-content:center;text-align:center;font-family:'Cinzel',serif;font-size:11px;line-height:1.35;color:var(--seal);padding:14px}
.title{position:absolute;left:182px;top:60px;font-family:'Cinzel',serif;color:var(--ink);line-height:1}
.title .edition{display:block;font-size:30px;color:var(--forest);margin-bottom:8px}
.title .edition sup{font-size:16px;vertical-align:top;position:relative;top:2px}
.title .event{display:block;font-size:27px;line-height:1.2}
.title .event.amp{font-size:36px}
.tagline{position:absolute;top:209px;left:0;width:100%;text-align:center;font-family:'Merriweather',serif;font-size:11.6px;letter-spacing:.2px;color:var(--ink);text-transform:uppercase}
.photo{position:absolute}
.p-dancer{left:0;top:242px;width:171px;height:188px;background:linear-gradient(160deg,#f2e6d8,#d9a23a 55%,#b5382c)}
.p-friends{left:173px;top:242px;width:341px;height:188px;background:linear-gradient(180deg,#e9e9e7,#3a3a3a 60%,#1c1c1c)}
.p-crowd{left:0;top:432px;width:184px;height:126px;background:linear-gradient(180deg,#d9d6d2,#6d6560)}
.p-drummer{left:186px;top:432px;width:97px;height:126px;background:linear-gradient(180deg,#f1ece8,#7b5a3c 60%,#3b2218)}
.p-tables{left:285px;top:432px;width:229px;height:126px;background:linear-gradient(180deg,#cfc6c3,#7a3b45 60%,#3b2f5b)}
.band{position:absolute;left:0;top:558px;width:100%;height:180px;background:var(--night)}
.theme{position:absolute;top:18px;width:100%;text-align:center;font-family:'Merriweather',serif;font-size:20px;line-height:1.35;color:var(--gold);text-transform:uppercase}
.theme q{text-transform:none}
.partner{position:absolute;left:28px;top:106px;display:flex;align-items:center;gap:6px}
.partner-name{font-family:'Merriweather',serif;font-size:15px;line-height:1.1;color:var(--harbor)}
.partner-dot{width:38px;height:38px;border:2px solid var(--harbor);border-radius:50%}
.details{position:absolute;right:31px;top:92px;text-align:right;font-family:'Merriweather',serif;color:var(--paper)}
.details .when{font-size:15px;font-weight:700}
.details .when span{font-weight:400}
.details .where{font-size:13px;margin-top:8px}
.details .address{font-size:13px;margin-top:14px}

/* back */
.intro{background:var(--orange);height:100px;padding:16px 26px 0 28px;font-family:'Merriweather',serif;font-size:11.4px;line-height:15.4px;letter-spacing:-.3px;text-align:justify;color:var(--ink)}
.section{padding:0 26px 0 28px;font-family:'Merriweather',serif;color:var(--ink)}
.section h2{font-size:12.6px;font-weight:900;margin-top:10px;margin-bottom:2px;letter-spacing:-.1px}
.section p{font-size:11.4px;line-height:15.4px;letter-spacing:-.3px;text-align:justify}
.section p.note{text-align:left}
.section p.gap{margin-top:8px}
.p-hall{left:0;bottom:0;width:514px;height:214px;background:linear-gradient(180deg,#cfcfcf 0%,#8a7d7a 40%,#7fce86 75%,#5a5560)}
</style>
</head>
<body>

<section class="page front">
  <p class="council-name">Shared Paths Youth Circle of Willow Basin’s</p>
  <div class="seal">Shared Paths Youth Circle</div>
  <h1 class="title">
    <span class="edition">13<sup>th</sup> Annual</span>
    <span class="event">Lantern Gathering</span>
    <span class="event amp">&amp; Summit</span>
  </h1>
  <p class="tagline">Teens expressing their faith through art, music, and dialogue</p>

  <div class="photo p-dancer" role="img" aria-label="Smiling dancer in a yellow and red costume"></div>
  <div class="photo p-friends" role="img" aria-label="Four teens making heart shapes with their hands"></div>
  <div class="photo p-crowd" role="img" aria-label="Students mingling in a community hall"></div>
  <div class="photo p-drummer" role="img" aria-label="Young drummer playing taiko drums"></div>
  <div class="photo p-tables" role="img" aria-label="Students in discussion around round tables"></div>

  <div class="band">
    <h2 class="theme">Interfaith Youth Forum<br>This year's theme <q>Is Religion Cool?</q></h2>
    <div class="partner">
      <span class="partner-name">Bright<br>Harbor<br>Allies</span>
      <span class="partner-dot"></span>
    </div>
    <div class="details">
      <p class="when">Sunday March 19<sup>th</sup>, 2017 <span>| 11:00am - 5:00pm</span></p>
      <p class="where">The Meridian Hall of Willow Basin</p>
      <p class="address">4190 Larkspur Ave, Willow Basin, CA 90000</p>
    </div>
  </div>
</section>

<section class="page back">
  <p class="intro">All high school age faith groups are invited to come and join with 150 to 175 other high school students from various faith traditions to participate in the Shared Paths Youth Circle of Willow Basin’s Annual Interfaith Youth Forum. More than ever, our county and world need young leaders who are willing to learn from each other and build stronger communities!</p>

  <div class="section">
    <h2>LANTERN SUMMIT</h2>
    <p>The purpose of this Interfaith Youth Forum is to bring together young people from diverse ethnic, cultural, and religious backgrounds, and to engage them in dialogue. True dialogue is a conversation on a common subject between two or more persons of differing points of view and/or backgrounds. We feel that this commitment to dialogue will affect relationships in a constructive way in our places of worship and in our community.</p>
    <p>The forum itself involves having eight religiously diverse high school-age students, one adult, and youth leader around each table to discuss common questions. Our youth leaders act as facilitators, but it is stressed that it is the students we want to hear from.</p>
    <p class="note">RSVP for our LANTERN SUMMIT by February 19th, 2017</p>

    <h2>LANTERN GATHERING</h2>
    <p>The forum will be followed by the Lantern Gathering where families of the participants are welcomed to join. The Gathering will include musical performances of all types from diverse religious communities. The differing performing arts include but are not limited to singing, dancing, instrumental music, storytelling, etc.</p>
    <p class="note gap">To Participate in our Lantern Gathering (Music, Song, Dance), RSVP by February 25th, 2017</p>

    <h2>ART GALLERY</h2>
    <p>This event will include and Art Gallery display of students’ work, highlighting their expressions of faith, and artwork promoting learning, understanding, leadership, and service. Art includes any painting, illustration, sculpture, photography or other visual art.</p>
    <p class="note">Art Work for our Art Galley must be submitted by: March 10th, 2017</p>
  </div>

  <div class="photo p-hall" role="img" aria-label="Crowded hall of students seated at round tables during the forum"></div>
</section>

</body>
</html>
```